Business Card for Home Inspection Company
Birchway Home Checks, Inc.
Professional
Martin Kovalenko
P.O. Box 8327
Hauppauge, NY 11594
Martin@BirchwayHomeChecks.com
www.BirchwayHomeChecks.com
Logo To Use...

```html
<!DOCTYPE html>
<html lang="en">
<head>
<meta charset="utf-8">
<title>Birchway Home Checks – Stationery Set</title>
<link href="https://fonts.googleapis.com/css2?family=Open+Sans:wght@400;600;700&display=swap" rel="stylesheet">
<style>
  :root{
    --navy:#2b4a9b;
    --slate:#6c6d73;
    --silver:#c9ccd3;
    --paper:#ffffff;
    --ink:#3a3d46;
    --ghost:#e8ebf2;
    --backdrop:#ecebe8;
  }
  *{margin:0;padding:0;box-sizing:border-box}
  html,body{width:1200px;height:599px;overflow:hidden}
  body{background:var(--backdrop);font-family:"Open Sans",Arial,sans-serif;color:var(--ink);position:relative}

  .sheet{position:absolute;background:var(--paper);box-shadow:0 2px 6px rgba(0,0,0,.18);overflow:hidden}
  .wordmark{font-family:"Open Sans",Arial,sans-serif;font-weight:700;color:var(--navy);white-space:nowrap;display:flex;align-items:center;gap:5px}
  .wordmark .dot{display:inline-block;border-radius:50%;background:var(--navy);flex:none}
  .wordmark.on-dark{color:var(--paper)}
  .wordmark.on-dark .dot{background:var(--paper)}
  .wave{position:absolute;left:0;width:100%;display:block}
  .fine{white-space:nowrap}

  /* business cards */
  .card-front{left:24px;top:240px;width:163px;height:86px}
  .card-front .wordmark{position:absolute;left:10px;top:9px;font-size:10px}
  .card-front .wordmark .dot{width:7px;height:7px}
  .card-front .details{position:absolute;right:8px;top:25px;font-size:4.6px;line-height:1.42;text-align:right}
  .card-front .details strong{font-size:5.4px;color:var(--navy)}
  .card-front .wave{bottom:0;height:22px}

  .card-back{left:24px;top:362px;width:163px;height:86px;background:var(--navy)}
  .card-back .wordmark{position:absolute;left:0;right:0;top:28px;justify-content:center;font-size:10px}
  .card-back .wordmark .dot{width:7px;height:7px}
  .card-back .web{position:absolute;left:0;right:0;top:60px;text-align:center;font-size:4.6px;color:var(--paper);letter-spacing:.3px}

  /* letterhead */
  .letterhead{left:216px;top:29px;width:350px;height:554px}
  .letterhead .wordmark{position:absolute;left:20px;top:22px;font-size:12px}
  .letterhead .wordmark .dot{width:8px;height:8px}
  .letterhead .contact{position:absolute;left:222px;top:18px;font-size:4.8px;line-height:1.6}
  .letterhead .ghost{position:absolute;left:0;right:0;top:155px;text-align:center;font-weight:700;font-size:24px;color:var(--ghost);white-space:nowrap}
  .letterhead .wave{bottom:0;height:96px}

  /* envelopes */
  .envelope{width:518px;height:132px;left:653px}
  .envelope .flap{position:absolute;left:0;top:0;width:100%;height:70px}
  .envelope .wordmark{position:absolute;left:0;right:0;justify-content:center;font-size:12px}
  .envelope .wordmark .dot{width:8px;height:8px}
  .env-blue{top:22px}
  .env-blue .wordmark{top:22px}
  .env-grey{top:120px}
  .env-grey .wordmark{top:30px}
  .env-white{top:222px}
  .env-white .wordmark{top:44px}

  .envelope-front{left:653px;top:356px;width:384px;height:190px}
  .envelope-front .wordmark{position:absolute;left:14px;top:14px;font-size:13px}
  .envelope-front .wordmark .dot{width:9px;height:9px}
  .envelope-front .return{position:absolute;left:34px;top:35px;font-size:4.6px;line-height:1.5}
  .envelope-front .ghost{position:absolute;left:0;right:0;top:112px;text-align:center;font-weight:700;font-size:20px;color:var(--ghost);white-space:nowrap}
</style>
</head>
<body>

<section class="sheet card-front" aria-label="Business card front">
  <div class="wordmark"><span class="dot"></span>Birchway Home Checks</div>
  <div class="details fine">
    <strong>Martin Kovalenko</strong><br>
    Licensed Inspector<br>
    P.O. Box 8327, Hauppauge, NY 11594<br>
    Tel 631-555-0148<br>
    Martin@BirchwayHomeChecks.com
  </div>
  <svg class="wave" viewBox="0 0 163 34" preserveAspectRatio="none" aria-hidden="true">
    <path d="M0 20 C50 4 110 26 163 6 L163 34 L0 34Z" fill="var(--navy)"/>
    <path d="M0 16 C50 0 110 22 163 2 L163 6 C110 26 50 4 0 20Z" fill="var(--slate)"/>
    <path d="M0 13 C50 -2 110 19 163 -1 L163 1 C110 21 50 1 0 15Z" fill="var(--silver)"/>
  </svg>
</section>

<section class="sheet card-back" aria-label="Business card back">
  <div class="wordmark on-dark"><span class="dot"></span>Birchway Home Checks</div>
  <div class="web">www.BirchwayHomeChecks.com</div>
</section>

<section class="sheet letterhead" aria-label="Letterhead">
  <div class="wordmark"><span class="dot"></span>Birchway Home Checks</div>
  <div class="contact fine">
    P.O. Box 8327, Hauppauge, NY 11594<br>
    Tel 631-555-0148<br>
    Fax 631-555-0149<br>
    Martin@BirchwayHomeChecks.com
  </div>
  <div class="ghost">Birchway Home Checks</div>
  <svg class="wave" viewBox="0 0 350 96" preserveAspectRatio="none" aria-hidden="true">
    <path d="M0 52 C110 20 230 70 350 28 L350 96 L0 96Z" fill="var(--navy)"/>
    <path d="M0 44 C110 12 230 62 350 20 L350 28 C230 70 110 20 0 52Z" fill="var(--slate)"/>
    <path d="M0 38 C110 6 230 55 350 14 L350 18 C230 59 110 10 0 42Z" fill="var(--silver)"/>
  </svg>
</section>

<section class="sheet envelope env-blue" aria-label="Envelope back, navy flap">
  <svg class="flap" viewBox="0 0 518 70" preserveAspectRatio="none" aria-hidden="true">
    <path d="M0 0 H518 V40 C380 70 140 70 0 40Z" fill="var(--navy)"/>
  </svg>
  <div class="wordmark on-dark"><span class="dot"></span>Birchway Home Checks</div>
</section>

<section class="sheet envelope env-grey" aria-label="Envelope back, grey flap">
  <svg class="flap" viewBox="0 0 518 70" preserveAspectRatio="none" aria-hidden="true">
    <path d="M0 0 H518 V44 C380 72 140 72 0 44Z" fill="var(--slate)"/>
  </svg>
  <div class="wordmark on-dark"><span class="dot"></span>Birchway Home Checks</div>
</section>

<section class="sheet envelope env-white" aria-label="Envelope back, white flap">
  <svg class="flap" viewBox="0 0 518 70" preserveAspectRatio="none" aria-hidden="true">
    <path d="M0 44 C140 72 380 72 518 44" fill="none" stroke="#d9dbe0" stroke-width="1.5"/>
  </svg>
  <div class="wordmark"><span class="dot"></span>Birchway Home Checks</div>
</section>

<section class="sheet envelope-front" aria-label="Envelope front">
  <div class="wordmark"><span class="dot"></span>Birchway Home Checks</div>
  <div class="return fine">
    P.O. Box 8327<br>
    Hauppauge, NY 11594
  </div>
  <div class="ghost">Birchway Home Checks</div>
</section>

</body>
</html>
```